****Business Card Design for Cormwell Development. Design based around attached logo/company name

I’m looking for business card design for my company Cormwell Development Group,LLC. Design should be professional, sharp and minimal. Outside of the attached logos, greyscale colors for remainder of cards. My thoughts are two-sided card with attached logo on one side and my info on the other but open to one-sided as well with right design.
Target Market(s)
Real estate professionals including banks, private investors, property owners, developers, commercial tenants like Brewlantic, Granvey or Tamsett’s.
Industry/Entity Type
Commercial real estate development and investments.
Contact Information for Business Card
Name, title, email, phone #’s, web address and physical address
Font styles to use
Other font styles liked:
- Helvetica, Garamond, etc
Colors
Designer to choose only greyscale colors for use in the design.
Requirements
Must have
- Attached logo first or second options.
Nice to have
- Two sided card with logo on one side. Attached Logo/company name can be laid out any way that flows as long as it’s legible.name
Should not have
- No loud colors. ***Please do not include logo, I have removed the company design with a logo image.

```html
<!DOCTYPE html>
<html lang="en">
<head>
<meta charset="utf-8">
<title>Cormwell Development Group, LLC — Business Cards</title>
<link rel="stylesheet" href="https://fonts.googleapis.com/css2?family=Cinzel:wght@400&family=Arimo:wght@400&display=swap">
<style>
  :root {
    --page-bg: #d4d5d8;
    --slate: #5a6276;
    --slate-text: #6d7385;
    --card-white: #ffffff;
    --ink: #3e4350;
    --light-on-slate: #eef0f4;
    --muted-on-slate: #a9afbd;
  }
  * { margin: 0; padding: 0; box-sizing: border-box; }
  html, body {
    width: 804px;
    height: 1200px;
    overflow: hidden;
    background: var(--page-bg);
  }
  .sheet {
    position: relative;
    width: 804px;
    height: 1200px;
  }
  .card {
    position: absolute;
    width: 660px;
    height: 377px;
    box-shadow: 0 10px 24px rgba(0, 0, 0, 0.22);
    overflow: hidden;
  }
  .card-front {
    left: 72px;
    top: 130px;
    background: var(--slate);
  }
  .card-back {
    left: 72px;
    top: 680px;
    background: var(--card-white);
  }

  .company-name {
    position: absolute;
    left: 0;
    right: 0;
    font-family: "Arimo", Helvetica, sans-serif;
    font-weight: 400;
    text-transform: uppercase;
    text-align: center;
    line-height: 1.2;
    white-space: nowrap;
  }
  .card-front .company-name {
    top: 172px;
    font-size: 23px;
    letter-spacing: 2px;
    color: var(--light-on-slate);
  }
  .card-back .company-name {
    top: 88px;
    font-size: 21px;
    letter-spacing: 2px;
    color: var(--slate-text);
  }

  .edge-tab {
    position: absolute;
    right: 0;
    top: 52px;
    width: 14px;
    height: 70px;
    background: var(--slate);
  }

  .name-band {
    position: absolute;
    left: 0;
    top: 212px;
    width: 282px;
    height: 86px;
    background: var(--slate);
    display: flex;
    flex-direction: column;
    justify-content: center;
    align-items: center;
  }
  .person-name {
    font-family: "Cinzel", serif;
    font-size: 22px;
    color: var(--light-on-slate);
    letter-spacing: 1px;
  }
  .person-title {
    font-family: "Cinzel", serif;
    font-size: 11px;
    color: var(--muted-on-slate);
    letter-spacing: 1.5px;
    margin-top: 3px;
  }

  .contact-list {
    position: absolute;
    left: 292px;
    top: 198px;
    list-style: none;
    font-family: "Arimo", Helvetica, sans-serif;
    font-size: 13px;
    color: var(--ink);
  }
  .contact-item {
    display: flex;
    align-items: flex-start;
    gap: 9px;
    margin-bottom: 7px;
    line-height: 16px;
  }
  .contact-icon {
    flex: none;
    width: 16px;
    height: 16px;
    background: var(--slate);
    border-radius: 2px;
  }
  .contact-icon svg { display: block; width: 16px; height: 16px; }
</style>
</head>
<body>
<main class="sheet">

  <section class="card card-front" aria-label="Business card front">
    <p class="company-name">Cormwell Development Group, LLC</p>
  </section>

  <section class="card card-back" aria-label="Business card back">
    <p class="company-name">Cormwell Development Group, LLC</p>

    <div class="edge-tab"></div>

    <div class="name-band">
      <div class="person-name">YOUR NAME</div>
      <div class="person-title">DESIGNATION</div>
    </div>

    <ul class="contact-list">
      <li class="contact-item">
        <span class="contact-icon">
          <svg viewBox="0 0 16 16"><path d="M5 3.5l2 2.2-1.1 1.3c.6 1.3 1.6 2.3 2.9 2.9l1.3-1.1 2.2 2-1.2 1.7C7.6 12.3 3.7 8.4 3.5 4.7z" fill="#fff"/></svg>
        </span>
        +0000 712 4590
      </li>
      <li class="contact-item">
        <span class="contact-icon">
          <svg viewBox="0 0 16 16"><rect x="3.5" y="5" width="9" height="6.5" fill="none" stroke="#fff" stroke-width="1.2"/><path d="M3.5 5l4.5 3.6L12.5 5" fill="none" stroke="#fff" stroke-width="1.2"/></svg>
        </span>
        info@cormwelldev.com
      </li>
      <li class="contact-item">
        <span class="contact-icon">
          <svg viewBox="0 0 16 16"><circle cx="8" cy="8" r="4.6" fill="none" stroke="#fff" stroke-width="1.1"/><ellipse cx="8" cy="8" rx="2" ry="4.6" fill="none" stroke="#fff" stroke-width="1"/><path d="M3.4 8h9.2" stroke="#fff" stroke-width="1"/></svg>
        </span>
        www.cormwelldev.com
      </li>
      <li class="contact-item">
        <span class="contact-icon">
          <svg viewBox="0 0 16 16"><path d="M8 13.2S4.4 9.2 4.4 6.8a3.6 3.6 0 017.2 0C11.6 9.2 8 13.2 8 13.2z" fill="#fff"/><circle cx="8" cy="6.8" r="1.3" fill="#5a6276"/></svg>
        </span>
        <span>Your City Address, Street Location<br>NY City, USA</span>
      </li>
    </ul>
  </section>

</main>
</body>
</html>
```